Tribe as pace "La tribu marca el paso"

I'm writing a book about word of mouth and the consumer as the media "the book is in Spanish" so you have to use "La tribu marca el paso" the subtitle is and 30 examples that proves it "Más 30 relatos de la plaza"

Book is about the power of consumer nowadays , the book will combine the era of social media but also the power of one to one word of mouth meaning w/o being connected to an electronic platform

Tribe sets the pace is a book about the power that now the consumer has in this double way interaction between the brands and the consumer, between the services and the people between the social media and the traditional media.

Consumer is on control and it is because "tribe sets the pace"

About book principles
I love simple books white background, simplicity around the fonts and the images (simple is better)

Target Market(s)

Marketing and digital marketing managers, social media managers, community managers, social media agencies, business people

Industry/Entity Type

Electronic

Requirements
Must have
• White backgroung, black and red fonts big fonts
Nice to have
• the subtitle "Más 30 relatos de la calle"

```html
<!DOCTYPE html>
<html lang="es">
<head>
<meta charset="utf-8">
<title>La tribu marca el paso — cubierta</title>
<link rel="stylesheet" href="https://fonts.googleapis.com/css2?family=Anton&family=Dosis:wght@300;400;800&family=Quicksand:wght@400;500;700&display=swap">
<style>
  :root {
    --backdrop: #ecebe8;
    --paper: #ffffff;
    --ink: #141414;
    --spine: #0d0d0d;
    --spine-text: #ffffff;
    --red: #d0121b;
  }
  * { margin: 0; padding: 0; box-sizing: border-box; }
  html, body {
    width: 1200px;
    height: 983px;
    overflow: hidden;
    background: var(--backdrop);
  }
  .book {
    position: absolute;
    left: 250px;
    top: 50px;
    width: 700px;
    height: 883px;
    display: flex;
    box-shadow: 0 10px 30px rgba(0,0,0,0.14);
  }
  .spine {
    position: relative;
    width: 60px;
    height: 100%;
    background: var(--spine);
    display: flex;
    align-items: center;
    justify-content: center;
  }
  .spine__label {
    writing-mode: vertical-rl;
    font-family: "Anton", sans-serif;
    font-size: 26px;
    letter-spacing: 0.5px;
    white-space: nowrap;
    color: var(--spine-text);
  }
  .spine__title { color: var(--red); }
  .cover {
    position: relative;
    width: 640px;
    height: 100%;
    background: var(--paper);
    color: var(--ink);
  }
  .tagline {
    position: absolute;
    left: 60px;
    top: 66px;
    font-family: "Quicksand", sans-serif;
    font-weight: 500;
    font-size: 17px;
    letter-spacing: 1.5px;
    text-transform: uppercase;
  }
  .title {
    position: absolute;
    left: 150px;
    top: 150px;
    font-family: "Dosis", sans-serif;
    text-transform: uppercase;
    line-height: 1;
  }
  .title__lead {
    display: block;
    font-weight: 800;
    font-size: 104px;
    letter-spacing: 4px;
  }
  .title__main {
    display: block;
    font-weight: 400;
    font-size: 74px;
    color: var(--red);
    letter-spacing: 1px;
    margin-top: 4px;
  }
  .title__tail {
    display: block;
    font-weight: 300;
    font-size: 50px;
    letter-spacing: 4px;
    margin-top: 6px;
    margin-left: 64px;
  }
  .network {
    position: absolute;
    left: 245px;
    top: 430px;
    width: 250px;
    height: 260px;
    border-radius: 12px;
    background: radial-gradient(circle at 50% 50%, #f3dccd 0%, #eef4f9 60%, var(--paper) 100%);
  }
  .subtitle {
    position: absolute;
    left: 0;
    right: 0;
    top: 720px;
    text-align: center;
    font-family: "Quicksand", sans-serif;
    font-weight: 500;
    font-size: 21px;
    color: var(--red);
    letter-spacing: 1px;
    text-transform: uppercase;
  }
  .author {
    position: absolute;
    right: 70px;
    top: 780px;
    font-family: "Quicksand", sans-serif;
    font-size: 19px;
    letter-spacing: 3px;
    text-transform: uppercase;
    line-height: 1.35;
  }
  .author__by { display: block; padding-left: 54px; }
  .edition {
    position: absolute;
    left: 22px;
    bottom: 30px;
    writing-mode: vertical-rl;
    font-family: "Anton", sans-serif;
    font-size: 17px;
    letter-spacing: 0.5px;
    text-transform: uppercase;
    color: var(--ink);
  }
  .edition sup { font-size: 11px; }
</style>
</head>
<body>
  <div class="book">
    <aside class="spine">
      <p class="spine__label"><span class="spine__title">La tribu marca el paso</span> Por Julián Robledo</p>
    </aside>
    <main class="cover">
      <p class="tagline">El poder de uno a uno el boca a boca</p>
      <h1 class="title">
        <span class="title__lead">La tribu</span>
        <span class="title__main">marca</span>
        <span class="title__tail">el paso</span>
      </h1>
      <div class="network" role="img" aria-label="Ilustración de una red de personas conectadas por líneas punteadas"></div>
      <p class="subtitle">Más 30 relatos de la calle</p>
      <p class="author"><span class="author__by">Por</span>Julián Robledo</p>
      <p class="edition">1<sup>a</sup> edición</p>
    </main>
  </div>
</body>
</html>
```